Web design for an intellectual property law practice

I need to design a simple landing page that may in the future expand to a full site. It should be very high tech focused.

Target Market(s)

Anyone seeking legal services

Industry/Entity Type

Legal

Number of Pages Required

2 page

Font styles to use
Other font styles liked:
• The same font as my logo

Colors
ec1f27

Requirements
Must have
• My logo (see attached).
Nice to have
• Open to ideas.

```html
<!DOCTYPE html>
<html lang="en">
<head>
<meta charset="utf-8">
<title>Brightclaim Patent Law</title>
<link href="https://fonts.googleapis.com/css2?family=Montserrat:wght@300;400;500;600;700&family=Open+Sans:wght@400;600&display=swap" rel="stylesheet">
<style>
:root{
  --red:#ec1f27;
  --red-dark:#c4161d;
  --ink:#1b1b1d;
  --ink-soft:#2a2a2e;
  --text:#444448;
  --muted:#8a8a90;
  --line:#dcdcdf;
  --paper:#ffffff;
  --mist:#f3f3f4;
  --footer:#e9e9eb;
}
*{box-sizing:border-box;margin:0;padding:0}
html,body{width:1200px;height:2432px;overflow:hidden}
body{font-family:"Open Sans",Arial,sans-serif;color:var(--text);background:var(--paper)}
.brand{font-family:"Montserrat",Arial,sans-serif;font-weight:600;display:flex;align-items:center;gap:10px}
.brand-dot{width:14px;height:14px;border-radius:50%;background:var(--red)}

/* Hero */
.hero{position:relative;height:680px;background:linear-gradient(120deg,#1a1a1c 0%,#2b2b2f 55%,#3a3a3f 100%);overflow:hidden}
.hero-photo{position:absolute;right:60px;top:0;width:480px;height:660px;background:linear-gradient(180deg,#4a4a50 0%,#2c2c31 70%,#202024 100%)}
.nav{position:absolute;top:0;left:0;right:0;height:90px;display:flex;align-items:center;padding:0 60px;z-index:2}
.nav .brand{color:#fff;font-size:18px}
.nav-links{display:flex;gap:34px;margin-left:170px;font-family:"Montserrat",sans-serif;font-size:12px;font-weight:500;letter-spacing:1px;color:#fff}
.nav-phone{margin-left:auto;display:flex;align-items:center;gap:10px;color:#fff;font-family:"Montserrat",sans-serif;font-size:17px;font-weight:500}
.hero-copy{position:absolute;left:60px;top:270px;width:560px;z-index:2}
.hero h1{font-family:"Montserrat",sans-serif;font-weight:400;font-size:40px;letter-spacing:2px;color:#fff}
.hero p{margin-top:18px;font-size:13px;line-height:1.7;color:#c9c9ce;width:470px}
.hero-actions{margin-top:34px;display:flex;gap:24px}
.btn{display:inline-block;font-family:"Montserrat",sans-serif;font-weight:600;font-size:13px;letter-spacing:1px;padding:16px 40px;text-decoration:none}
.btn-dark{background:#111;color:#fff}
.btn-red{background:var(--red);color:#fff;padding:16px 56px}
.hero-bar{position:absolute;left:0;right:0;bottom:0;height:20px;background:var(--red)}
.hero-dots{position:absolute;right:24px;top:540px;display:flex;flex-direction:column;gap:8px}
.hero-dots span{width:6px;height:6px;border-radius:50%;background:#777}
.hero-dots span.on{background:var(--red)}

/* About */
.about{height:340px;display:flex;align-items:center;padding:0 0 0 330px}
.about .brand{color:var(--ink);font-size:20px;width:210px}
.about-divider{width:3px;height:190px;background:var(--red);margin:0 50px 0 40px}
.about-body{width:460px}
.about-body h2{font-family:"Montserrat",sans-serif;font-size:17px;font-weight:600;color:var(--ink)}
.about-body p{margin-top:16px;font-size:12px;line-height:1.8;color:var(--muted)}
.link-red{display:inline-block;margin-top:16px;font-family:"Montserrat",sans-serif;font-size:11px;font-weight:600;color:var(--red);text-decoration:none}

/* Practice areas */
.practice{height:530px;background:var(--mist);padding-top:60px;text-align:center}
.section-title{font-family:"Montserrat",sans-serif;font-weight:700;font-size:30px;color:var(--ink);letter-spacing:1px}
.section-sub{margin:14px auto 0;width:520px;font-size:12px;line-height:1.7;color:var(--muted)}
.areas{display:grid;grid-template-columns:repeat(4,210px);column-gap:60px;row-gap:58px;justify-content:center;margin-top:62px;text-align:left}
.area svg{width:32px;height:32px}
.area h3{margin-top:14px;font-family:"Montserrat",sans-serif;font-size:13px;font-weight:600;color:var(--ink)}
.area p{margin-top:6px;font-size:11px;line-height:1.6;color:var(--muted);width:170px}
.area .link-red{margin-top:8px}

/* Contact band */
.contact-band{height:340px;background:linear-gradient(180deg,#141416 0%,#24242a 100%);text-align:center;color:#fff;padding-top:70px}
.contact-band .pre{font-family:"Montserrat",sans-serif;font-weight:300;font-size:30px}
.contact-band h2{font-family:"Montserrat",sans-serif;font-weight:600;font-size:46px;letter-spacing:1px;margin-top:4px}
.contact-band .phone{font-family:"Montserrat",sans-serif;font-size:24px;font-weight:500;margin-top:12px}
.contact-line{display:flex;justify-content:center;align-items:center;gap:8px;font-size:11px;color:#b9b9bf;margin-top:12px}

/* Form */
.enquiry{height:440px;text-align:center;padding-top:34px}
.enquiry .pre{font-family:"Montserrat",sans-serif;font-weight:400;font-size:22px;color:var(--ink)}
.enquiry h2{font-family:"Montserrat",sans-serif;font-weight:500;font-size:38px;color:var(--ink);margin-top:2px}
.form{width:480px;margin:26px auto 0;display:grid;grid-template-columns:1fr 1fr;gap:14px}
.field{height:36px;border:1px solid var(--line);text-align:left;padding:10px 12px;font-size:11px;color:var(--muted)}
.field.wide{grid-column:1 / 3;height:110px}
.submit{grid-column:1 / 3;justify-self:center;margin-top:10px;background:#111;color:#fff;font-family:"Montserrat",sans-serif;font-size:11px;font-weight:600;padding:10px 22px;border-radius:3px;border:none}

/* Footer */
.footer{height:102px;background:var(--footer);display:flex;align-items:center;justify-content:center;font-size:11px;color:var(--muted)}
</style>
</head>
<body>

<header class="hero">
  <div class="hero-photo" role="img" aria-label="Photograph of two lawyers in business suits standing in an office"></div>
  <nav class="nav">
    <div class="brand"><span class="brand-dot"></span>Brightclaim Patent Law</div>
    <div class="nav-links"><span>HOME</span><span>ABOUT US</span><span>PRACTICE AREAS</span><span>CONTACT US</span></div>
    <div class="nav-phone">
      <svg width="18" height="18" viewBox="0 0 24 24"><path fill="#ec1f27" d="M6.6 10.8a15 15 0 0 0 6.6 6.6l2.2-2.2c.3-.3.7-.4 1-.2 1.1.4 2.3.6 3.6.6.6 0 1 .4 1 1V20c0 .6-.4 1-1 1A17 17 0 0 1 3 4c0-.6.4-1 1-1h3.5c.6 0 1 .4 1 1 0 1.3.2 2.5.6 3.6.1.3 0 .7-.2 1z"/></svg>
      +971 555 010 2040
    </div>
  </nav>
  <div class="hero-copy">
    <h1>Experience. Reputation. Results.</h1>
    <p>We protect the ideas, inventions and brands that drive modern business, with counsel built for technology companies at every stage.</p>
    <div class="hero-actions">
      <a class="btn btn-dark" href="#">LEARN MORE</a>
      <a class="btn btn-red" href="#">CONTACT US</a>
    </div>
  </div>
  <div class="hero-dots"><span class="on"></span><span></span><span></span></div>
  <div class="hero-bar"></div>
</header>

<section class="about">
  <div class="brand"><span class="brand-dot"></span>Brightclaim Patent Law</div>
  <div class="about-divider"></div>
  <div class="about-body">
    <h2>Intellectual Property Law</h2>
    <p>We advise inventors, founders and established firms on every stage of protecting their ideas. From first filing to enforcement, our team combines legal depth with real technical knowledge, so your patents, marks and designs are secured quickly and defended firmly across local and global markets.</p>
    <a class="link-red" href="#">Read More ›</a>
  </div>
</section>

<section class="practice">
  <h2 class="section-title">PRACTICE AREAS</h2>
  <p class="section-sub">Focused counsel for every form of intellectual property, from early filings to disputes.</p>
  <div class="areas">
    <div class="area">
      <svg viewBox="0 0 32 32"><circle cx="16" cy="16" r="13" fill="none" stroke="#ec1f27" stroke-width="2.5"/><path d="M20 12.5a5 5 0 1 0 0 7" fill="none" stroke="#ec1f27" stroke-width="2.5"/></svg>
      <h3>COPYRIGHT</h3><p>Clear advice to register and protect your work.</p><a class="link-red" href="#">Learn more ›</a>
    </div>
    <div class="area">
      <svg viewBox="0 0 32 32"><circle cx="16" cy="16" r="13" fill="none" stroke="#ec1f27" stroke-width="2.5"/><path d="M3 16h26M16 3c4 4 4 22 0 26M16 3c-4 4-4 22 0 26" fill="none" stroke="#ec1f27" stroke-width="2"/></svg>
      <h3>DOMAIN NAMES</h3><p>Secure and recover the web addresses you own.</p><a class="link-red" href="#">Learn more ›</a>
    </div>
    <div class="area">
      <svg viewBox="0 0 32 32"><path d="M16 3l3.8 8 8.7 1-6.4 6 1.7 8.6L16 22.3 8.2 26.6 9.9 18 3.5 12l8.7-1z" fill="#ec1f27"/></svg>
      <h3>ENTERTAINMENT LAW</h3><p>Contracts and rights for creators and studios.</p><a class="link-red" href="#">Learn more ›</a>
    </div>
    <div class="area">
      <svg viewBox="0 0 32 32"><path d="M9 5h14l6 8-13 15L3 13z" fill="none" stroke="#ec1f27" stroke-width="2.5" stroke-linejoin="round"/><path d="M3 13h26" stroke="#ec1f27" stroke-width="2"/></svg>
      <h3>INTELLECTUAL PROPERTY</h3><p>Strategy to build and guard your valuable assets.</p><a class="link-red" href="#">Learn more ›</a>
    </div>
    <div class="area">
      <svg viewBox="0 0 32 32"><rect x="4" y="7" width="24" height="18" rx="2" fill="none" stroke="#ec1f27" stroke-width="2.5"/><path d="M8 13h10M8 18h14" stroke="#ec1f27" stroke-width="2"/></svg>
      <h3>LICENSING LAW</h3><p>Fair agreements that let your ideas earn more.</p><a class="link-red" href="#">Learn more ›</a>
    </div>
    <div class="area">
      <svg viewBox="0 0 32 32"><path d="M8 3h12l6 6v20H8z" fill="none" stroke="#ec1f27" stroke-width="2.5" stroke-linejoin="round"/><path d="M12 15h10M12 20h10M12 25h6" stroke="#ec1f27" stroke-width="2"/></svg>
      <h3>PATENTS</h3><p>Drafting, filing and prosecution for new inventions.</p><a class="link-red" href="#">Learn more ›</a>
    </div>
    <div class="area">
      <svg viewBox="0 0 32 32"><rect x="7" y="14" width="18" height="14" rx="2" fill="none" stroke="#ec1f27" stroke-width="2.5"/><path d="M11 14V10a5 5 0 0 1 10 0v4" fill="none" stroke="#ec1f27" stroke-width="2.5"/></svg>
      <h3>TRADE SECRETS</h3><p>Keep confidential know how safe from misuse.</p><a class="link-red" href="#">Learn more ›</a>
    </div>
    <div class="area">
      <svg viewBox="0 0 32 32"><circle cx="16" cy="16" r="13" fill="none" stroke="#ec1f27" stroke-width="2.5"/><path d="M10 12h8M14 12v10M19 22v-10l3 5 3-5v10" fill="none" stroke="#ec1f27" stroke-width="1.8"/></svg>
      <h3>TRADEMARKS</h3><p>Search, register and enforce the names you trade.</p><a class="link-red" href="#">Learn more ›</a>
    </div>
  </div>
</section>

<section class="contact-band" role="img" aria-label="Dark photograph of hands working on a laptop">
  <p class="pre">Have More Questions?</p>
  <h2>CONTACT US TODAY</h2>
  <p class="phone">+971 555 010 2040</p>
  <p class="contact-line"><svg width="12" height="12" viewBox="0 0 24 24"><rect x="2" y="5" width="20" height="14" fill="none" stroke="#ec1f27" stroke-width="2"/><path d="M2 5l10 8 10-8" fill="none" stroke="#ec1f27" stroke-width="2"/></svg>info@brightclaimlaw.com</p>
  <p class="contact-line"><svg width="12" height="12" viewBox="0 0 24 24"><path d="M12 2a7 7 0 0 0-7 7c0 5 7 13 7 13s7-8 7-13a7 7 0 0 0-7-7zm0 9.5A2.5 2.5 0 1 1 12 6.5a2.5 2.5 0 0 1 0 5z" fill="#ec1f27"/></svg>Office 12, Harbour Tower, Dubai</p>
</section>

<section class="enquiry">
  <p class="pre">Get In Touch</p>
  <h2>Contact Us</h2>
  <form class="form">
    <div class="field">First Name</div>
    <div class="field">Last Name</div>
    <div class="field">Email</div>
    <div class="field">Phone</div>
    <div class="field wide">Message</div>
    <button class="submit" type="button">Submit</button>
  </form>
</section>

<footer class="footer">Copyright © 2024 Brightclaim Patent Law. All Rights Reserved.</footer>

</body>
</html>
```